Business Card Design Project

parking lot sealing and striping company

Industry/Entity Type

Business

Contact Information for Business Card

See pics below, blue and gray colors

```html
<!DOCTYPE html>
<html lang="en">
<head>
<meta charset="utf-8">
<title>Summit Crest Paving – Business Card</title>
<link href="https://fonts.googleapis.com/css2?family=Oswald:wght@600&family=Roboto+Condensed:wght@400&family=Rubik:wght@500&display=swap" rel="stylesheet">
<style>
  :root {
    --stage: #1a1a1a;
    --card: #fbfbfb;
    --navy: #0f2a3d;
    --blue: #1b95d8;
    --asphalt-dark: #1f2122;
    --asphalt-mid: #3a3c3d;
    --list-text: #f2f2f2;
  }
  html, body {
    margin: 0;
    padding: 0;
    width: 1200px;
    height: 767px;
    overflow: hidden;
    background: var(--stage);
  }
  .card {
    position: absolute;
    left: 376px;
    top: 247px;
    width: 446px;
    height: 270px;
    background: var(--card);
    overflow: hidden;
  }
  .asphalt {
    position: absolute;
    left: 0;
    top: 0;
    width: 200px;
    height: 270px;
  }
  .services {
    position: absolute;
    left: 30px;
    top: 57px;
    margin: 0;
    padding: 0;
    list-style: none;
    font-family: "Rubik", sans-serif;
    font-weight: 500;
    font-size: 13px;
    line-height: 19px;
    color: var(--list-text);
  }
  .services li::before {
    content: "»";
    display: inline-block;
    width: 11px;
    font-size: 11px;
  }
  .brand {
    position: absolute;
    left: 218px;
    top: 40px;
    display: flex;
    align-items: center;
    gap: 8px;
    font-family: "Rubik", sans-serif;
    font-weight: 500;
    font-size: 17px;
    color: var(--blue);
    line-height: 1.1;
  }
  .brand-dot {
    width: 40px;
    height: 40px;
    border-radius: 50%;
    background: var(--navy);
    flex: none;
  }
  .person {
    position: absolute;
    left: 218px;
    top: 124px;
  }
  .person-name {
    margin: 0;
    font-family: "Oswald", sans-serif;
    font-weight: 600;
    font-size: 18px;
    line-height: 22px;
    color: var(--navy);
    letter-spacing: -0.2px;
  }
  .person-role {
    margin: 1px 0 0;
    font-family: "Roboto Condensed", sans-serif;
    font-size: 10px;
    color: var(--navy);
  }
  .contact {
    position: absolute;
    left: 218px;
    top: 180px;
    font-family: "Roboto Condensed", sans-serif;
    font-size: 11px;
    color: var(--navy);
  }
  .address { margin: 0 0 8px; }
  .contact-row {
    display: flex;
    align-items: center;
    height: 16px;
  }
  .contact-row svg {
    width: 9px;
    height: 9px;
    margin-right: 11px;
    fill: var(--blue);
  }
</style>
</head>
<body>
  <div class="card">
    <svg class="asphalt" viewBox="0 0 200 270" role="img" aria-label="Textured dark asphalt surface with rough torn edge">
      <defs>
        <linearGradient id="asphaltTone" x1="0" y1="0" x2="1" y2="1">
          <stop offset="0" stop-color="#3a3c3d"/>
          <stop offset="1" stop-color="#1f2122"/>
        </linearGradient>
      </defs>
      <polygon fill="url(#asphaltTone)" points="0,0 190,0 186,10 184,25 190,50 194,77 185,100 172,137 176,169 165,190 160,209 152,232 148,249 138,270 0,270"/>
    </svg>

    <ul class="services">
      <li>Asphal Bealing</li>
      <li>Crack Repair</li>
      <li>Ramp Building</li>
      <li>Line Paiing</li>
      <li>Walevwe</li>
      <li>Asphal Bealing</li>
      <li>Crack Repair</li>
      <li>Ramp Building</li>
      <li>Line Paiing</li>
      <li>Walevwe</li>
    </ul>

    <div class="brand">
      <span class="brand-dot"></span>
      <span class="brand-name">Summit Crest<br>Paving</span>
    </div>

    <div class="person">
      <h1 class="person-name">MARK ELLISON</h1>
      <p class="person-role">Managing Director</p>
    </div>

    <div class="contact">
      <p class="address">4/12 Harbourline Court, VIC 3152</p>
      <div class="contact-row">
        <svg viewBox="0 0 10 10"><path d="M1 3.5C1 2 3 1.5 5 1.5S9 2 9 3.5L7.5 4V3.3H2.5V4ZM2.5 4.5H7.5L8.5 8.5H1.5Z"/></svg>
        <span>Free Call: 1800 SUMMIT</span>
      </div>
      <div class="contact-row">
        <svg viewBox="0 0 10 10"><path d="M0.5 2H9.5V8H0.5Z M1.2 2.6L5 5.5L8.8 2.6" stroke="#fbfbfb" stroke-width="0.8"/></svg>
        <span>mark@summitcrestpaving.com</span>
      </div>
      <div class="contact-row">
        <svg viewBox="0 0 10 10"><circle cx="5" cy="5" r="4.5"/><path d="M0.5 5H9.5M5 0.5V9.5M1.5 3H8.5M1.5 7H8.5" stroke="#fbfbfb" stroke-width="0.6" fill="none"/></svg>
        <span>www.summitcrestpaving.com</span>
      </div>
    </div>
  </div>
</body>
</html>
```